Web Design Project

blaze guard safety & solutions needs a new web design to go with its new logo design

we provide services such as instillation of fire sprinklers, fire hydrants , fire hose reels as well as fire extinguishers and fire blankets.

we can service these as well and also do the preventitave maintaince of these too.

we can do flow testing of sprinklers,hydrants & hosereels and test back flow prevention devices as well

old page is bgss-example.com.au

Industry/Entity Type

Defence

```html
<!DOCTYPE html>
<html lang="en">
<head>
<meta charset="utf-8">
<title>Blaze Guard Safety &amp; Solutions Pty Ltd</title>
<link rel="stylesheet" href="https://fonts.googleapis.com/css2?family=Bebas+Neue&family=Lora:wght@400&family=Open+Sans:wght@400;600&display=swap">
<style>
:root{
  --red-dark:#9c1b24;
  --red:#b8232d;
  --red-light:#d03a42;
  --cream:#fdf0d6;
  --heading:#8a1a1e;
  --text:#3a2a22;
  --muted:#5a4a40;
  --rule:#d8c7aa;
  --white:#ffffff;
  --gold:#f4cf8c;
}
*{margin:0;padding:0;box-sizing:border-box}
html,body{width:1200px;height:1057px;overflow:hidden}
body{background:var(--cream);font-family:"Open Sans",Arial,sans-serif;color:var(--text);position:relative}
.header-band{position:absolute;left:0;top:0;width:1200px;height:334px;
  background:radial-gradient(ellipse at 50% 20%,#b52530 0%,var(--red-dark) 60%,#8e1820 100%)}
.brand{position:absolute;top:44px;left:0;width:1200px;text-align:center;color:var(--white)}
.brand-mark{display:inline-flex;align-items:center;gap:12px;font-family:"Open Sans",sans-serif;font-weight:600;font-size:46px;letter-spacing:2px;line-height:1}
.brand-mark .square{width:26px;height:26px;background:var(--white)}
.brand-name{font-weight:600;font-size:13px;letter-spacing:.5px;margin-top:10px;color:#1a0a0a}
.brand-tag{font-weight:600;font-size:9px;margin-top:2px;color:var(--white)}
.main-nav{position:absolute;left:140px;top:154px;width:920px;height:50px;z-index:3;
  background:linear-gradient(#cf3a42,#a91d27);border-radius:3px;box-shadow:0 3px 6px rgba(0,0,0,.35);
  display:flex;align-items:center;justify-content:space-around;padding:0 14px}
.main-nav a{font-family:"Lora",serif;font-size:18px;color:var(--white);text-decoration:none;flex:1;text-align:center;
  border-left:1px solid rgba(255,255,255,.2)}
.main-nav a:first-child{border-left:none}
.hero{position:absolute;left:118px;top:180px;width:962px;height:314px;z-index:2;
  background:radial-gradient(ellipse at 40% 60%,#f3a12a 0%,#d9531a 45%,#8c1e0e 100%)}
.hero-title{position:absolute;left:66px;top:112px;font-family:"Bebas Neue",sans-serif;font-weight:400;line-height:1.05}
.hero-title .line1{font-size:60px;color:#fff3dc;display:block}
.hero-title .line2{font-size:54px;color:var(--gold);display:block}
.products{position:absolute;left:118px;top:494px;width:962px;height:122px;z-index:2;
  background:linear-gradient(#c93840,#a81f29);border-radius:0 0 8px 8px;display:flex}
.product{flex:1;text-align:center;border-left:1px solid rgba(0,0,0,.15);padding-top:14px}
.product:first-child{border-left:none}
.product-img{display:block;margin:0 auto;width:62px;height:62px;border-radius:8px;
  background:linear-gradient(#e8e2dc,#9b8f88)}
.product-img.red{background:linear-gradient(#f0473c,#a8121a)}
.product-label{font-family:"Lora",serif;font-size:18px;color:var(--white);margin-top:12px;display:block}
.welcome{position:absolute;left:122px;top:646px}
.welcome h1{font-family:"Open Sans",sans-serif;font-weight:400;font-size:34px;color:var(--heading);line-height:1.1}
.welcome p{font-size:18px;color:var(--text)}
.quote-btn{position:absolute;left:796px;top:641px;width:284px;height:60px;border-radius:8px;
  background:linear-gradient(#c6323b,#9a1820);box-shadow:0 2px 4px rgba(0,0,0,.3);
  display:flex;align-items:center;gap:14px;padding-left:18px;color:var(--white);font-size:23px;text-decoration:none}
.intro{position:absolute;left:120px;top:738px;width:962px;font-size:13.4px;line-height:25px;color:var(--text)}
.intro p{margin-bottom:25px}
.footer{position:absolute;left:120px;top:995px;width:942px;border-top:1px solid var(--rule);
  display:flex;justify-content:space-between;padding-top:10px}
.copyright{font-size:14px;color:var(--text);margin-top:4px}
.footer-nav{display:flex;gap:34px;margin-right:8px}
.footer-nav a{font-size:14px;color:var(--muted);text-decoration:none}
</style>
</head>
<body>
<div class="header-band"></div>
<header class="brand">
  <div class="brand-mark"><span class="square"></span>BGSS</div>
  <div class="brand-name">BLAZE GUARD SAFETY &amp; SOLUTIONS PTY LTD</div>
  <div class="brand-tag">YOUR BEST DEFENCE AGAINST FIRE</div>
</header>
<nav class="main-nav">
  <a href="#">Home</a><a href="#">Service</a><a href="#">Testing</a><a href="#">Products</a><a href="#">Contact us</a><a href="#">Testimonials</a><a href="#">FAQ'S</a>
</nav>
<section class="hero" role="img" aria-label="Firefighter in protective gear spraying a hose into a wall of flames">
  <h2 class="hero-title"><span class="line1">YOUR BEST DEFENCE</span><span class="line2">AGAINST FIRE</span></h2>
</section>
<section class="products">
  <div class="product"><span class="product-img" role="img" aria-label="Fire sprinkler head"></span><span class="product-label">fire sprinklers</span></div>
  <div class="product"><span class="product-img red" role="img" aria-label="Red fire hydrant"></span><span class="product-label">fire hydrants</span></div>
  <div class="product"><span class="product-img red" role="img" aria-label="Fire hose reel"></span><span class="product-label">fire hose reels</span></div>
  <div class="product"><span class="product-img red" role="img" aria-label="Fire blanket pouch"></span><span class="product-label">fire blankets</span></div>
  <div class="product"><span class="product-img red" role="img" aria-label="Fire extinguisher"></span><span class="product-label">fire extinguishers</span></div>
</section>
<section class="welcome">
  <h1>Welcome to</h1>
  <p>Blaze Guard Safety &amp; Solutions Pty Ltd</p>
</section>
<a class="quote-btn" href="#">
  <svg width="38" height="40" viewBox="0 0 38 40" aria-hidden="true">
    <rect x="3" y="3" width="24" height="32" rx="2" fill="#fff"/>
    <g stroke="#6a7fb0" stroke-width="2"><line x1="8" y1="11" x2="22" y2="11"/><line x1="8" y1="17" x2="22" y2="17"/><line x1="8" y1="23" x2="18" y2="23"/></g>
    <line x1="34" y1="14" x2="20" y2="34" stroke="#f2b33a" stroke-width="4"/>
  </svg>
  REQUEST QUOTE
</a>
<section class="intro">
  <p>At blaze guard we believe that no matter how large or small your business is we can help you with the design, installation and the maintenance of your system to the standard which it was designed to.</p>
  <p>Blaze Guard is a fire protection company situated on the Central Coast of NSW and is currently servicing the Sydney, Central Coast and Hunter areas, We are always looking for new clients who are not happy with there current service providers and are looking for a Competitive priced alternative. Blaze Guard will come to your site and assess your fire service assets and provide a full quotation on a 12 month service contract.</p>
  <p>Blaze Guard can also supply quotations for any alterations to your Sprinklers,Hydrants &amp; Hose reel systems along with your fire detection and emergency lighting.</p>
</section>
<footer class="footer">
  <p class="copyright">Copyright 2010 BGSS-EXAMPLE.COM.AU All Rights Reserved.</p>
  <nav class="footer-nav"><a href="#">Contact Us</a><a href="#">Request Quote</a><a href="#">Documents</a></nav>
</footer>
</body>
</html>
```